Need Two Flyers Created

I need two flyers created:
(1) Marketing me as a speaker with an upcoming book coming out including past topics I've spoken on with contact information - a pic of me will be included as well as a pic of the book; and
(2) marketing my new company - The Korvell Group, Inc., and our four pillars: Leadership Development, School Improvement, Superintendent/Central Office Support, and Strategic Advisory Services.

Target Market(s)

Educators
Business Leaders
Organization Leaders
Leaders in general

Industry/Entity Type

Marketing

Requirements
Must have
• Very creative but not overwhelming
• A picture of me
• A picture of the front of the book.

```html
<!DOCTYPE html>
<html lang="en">
<head>
<meta charset="utf-8">
<title>Purposeful Excellence – Speaker Flyer</title>
<link rel="stylesheet" href="https://fonts.googleapis.com/css2?family=Bebas+Neue&family=Oswald:wght@300;600&family=Tinos&family=Open+Sans:wght@400;600&display=swap">
<style>
  :root {
    --page: #eeeae4;
    --crimson: #c4274e;
    --pink: #e48aa1;
    --blue: #1f68ab;
    --plum: #8a3a78;
    --band: #2a2a2c;
    --gold: #f2cf5b;
    --white: #ffffff;
    --shadow: rgba(0,0,0,.28);
  }
  * { margin: 0; padding: 0; box-sizing: border-box; }
  html, body { width: 1200px; height: 1020px; overflow: hidden; background: var(--page); }
  .flyer {
    position: absolute; left: 40px; top: 113px; width: 1120px; height: 793px;
    overflow: hidden; box-shadow: 8px 10px 22px var(--shadow);
    font-family: "Open Sans", sans-serif; color: var(--white);
  }
  .flyer-bg { position: absolute; inset: 0; }
  .brand { position: absolute; left: 60px; top: 50px; font-family: "Tinos", serif; color: var(--white); line-height: 1; }
  .brand-the { font-size: 34px; letter-spacing: 2px; margin-left: 150px; }
  .brand-name { font-size: 74px; letter-spacing: 1px; }
  .brand-group { font-size: 30px; letter-spacing: 2px; margin-left: 268px; margin-top: 4px; }
  .title-band { position: absolute; left: 0; top: 271px; width: 467px; height: 241px; background: var(--band); }
  .title-main { position: absolute; left: 60px; top: 284px; font-family: "Bebas Neue", sans-serif; font-size: 104px; line-height: 1; letter-spacing: 1px; }
  .title-sub { position: absolute; left: 60px; top: 378px; font-family: "Oswald", sans-serif; font-weight: 300; font-size: 64px; line-height: 1; letter-spacing: 2px; }
  .author { position: absolute; left: 60px; top: 460px; font-family: "Tinos", serif; white-space: nowrap; }
  .author-name { font-size: 30px; color: var(--gold); }
  .author-degrees { font-size: 19px; margin-left: 12px; }
  .topics-label {
    position: absolute; left: 37px; top: 537px; width: 224px; height: 48px;
    background: var(--band); color: var(--gold);
    font-family: "Oswald", sans-serif; font-weight: 600; font-size: 32px; line-height: 48px; padding-left: 14px;
  }
  .topics { position: absolute; left: 56px; top: 602px; width: 540px; list-style: none; font-size: 13.5px; line-height: 1.45; }
  .topics li { position: relative; padding-left: 26px; margin-bottom: 10px; }
  .topics li svg { position: absolute; left: 0; top: 3px; }
  .contact { position: absolute; left: 64px; top: 748px; display: flex; align-items: center; font-size: 19px; }
  .contact-divider { width: 1px; height: 34px; background: var(--white); margin: 0 16px; }
  .social { display: flex; gap: 6px; }
  .social span { width: 22px; height: 22px; border-radius: 50%; background: var(--white); }
  .book-cover {
    position: absolute; left: 511px; top: 232px; width: 209px; height: 308px;
    background: linear-gradient(180deg, #9b8a7a 0%, #6f6258 38%, #f4f0ec 39%, #c4274e 62%, #f4f0ec 63%, #ffffff 100%);
    box-shadow: 6px 6px 14px var(--shadow);
  }
  .speaker-photo {
    position: absolute; left: 800px; top: 43px; width: 320px; height: 750px;
    background: linear-gradient(180deg, #6b4a3a 0%, #6b4a3a 22%, #bcd0e6 23%, #a9bfd9 78%, #2d2d33 79%, #2d2d33 100%);
    border-radius: 140px 140px 0 0;
  }
</style>
</head>
<body>
<main class="flyer">
  <svg class="flyer-bg" width="1120" height="793" viewBox="0 0 1120 793" aria-hidden="true">
    <defs>
      <linearGradient id="topGrad" x1="0" y1="0" x2="1" y2="0.3">
        <stop offset="0" stop-color="#c4274e"/>
        <stop offset="0.55" stop-color="#d4506f"/>
        <stop offset="1" stop-color="#e9a3b4"/>
      </linearGradient>
      <linearGradient id="lowGrad" x1="0" y1="0" x2="1" y2="0">
        <stop offset="0" stop-color="#1f68ab"/>
        <stop offset="0.5" stop-color="#6a4682"/>
        <stop offset="0.8" stop-color="#b02e5a"/>
        <stop offset="1" stop-color="#c4274e"/>
      </linearGradient>
    </defs>
    <rect width="1120" height="793" fill="url(#topGrad)"/>
    <polygon points="0,512 1120,333 1120,793 0,793" fill="url(#lowGrad)"/>
    <polygon points="467,271 1120,70 1120,430 467,512" fill="#ffffff" opacity="0.12"/>
  </svg>

  <div class="brand">
    <div class="brand-the">THE</div>
    <div class="brand-name">KORVELL</div>
    <div class="brand-group">GROUP</div>
  </div>

  <div class="title-band"></div>
  <h1 class="title-main">PURPOSEFUL</h1>
  <p class="title-sub">EXCELLENCE</p>
  <p class="author"><span class="author-name">S. Marlon Reeve</span><span class="author-degrees">(Ph.D. ’07, M.Ed. ’02)</span></p>

  <div class="book-cover" role="img" aria-label="Front cover of the book Purposeful Excellence: students around a classroom table above the title"></div>
  <div class="speaker-photo" role="img" aria-label="Portrait of the speaker in a light blue shirt and red tie, arms crossed"></div>

  <h2 class="topics-label">PAST TOPICS</h2>
  <ul class="topics">
    <li><svg width="12" height="12" viewBox="0 0 12 12"><rect x="0.5" y="0.5" width="11" height="11" fill="none" stroke="#fff"/><path d="M2.5 6 L5 8.5 L9.5 3" fill="none" stroke="#fff" stroke-width="1.5"/></svg>Lorem ipsum dolor sit amet, consectetur adipiscing elit, sed do eiusmod tempor incididunt ut labore et dolore magna aliqua.</li>
    <li><svg width="12" height="12" viewBox="0 0 12 12"><rect x="0.5" y="0.5" width="11" height="11" fill="none" stroke="#fff"/><path d="M2.5 6 L5 8.5 L9.5 3" fill="none" stroke="#fff" stroke-width="1.5"/></svg>But I must explain to you how all this mistaken idea of denouncing pleasure and praising pain was born and I will give you a complete account of the system, and expound the actual teachings of the great explorer of the truth, the master-builder of human happiness.</li>
  </ul>

  <div class="contact">
    <svg width="20" height="20" viewBox="0 0 20 20" style="margin-right:12px"><circle cx="10" cy="10" r="8.5" fill="none" stroke="#fff" stroke-width="1.4"/><ellipse cx="10" cy="10" rx="3.5" ry="8.5" fill="none" stroke="#fff" stroke-width="1.2"/><path d="M1.5 10 H18.5" stroke="#fff" stroke-width="1.2"/></svg>
    <span>www.website.com</span>
    <span class="contact-divider"></span>
    <span class="social"><span></span><span></span><span></span></span>
  </div>
</main>
</body>
</html>
```